Company website design for Marlowfen Pricing Counsel LLC

Design of company website. See uploaded outline. Logo hex codes for the icon colors: middle blue - 4D6C8A, dark blue - 11122B.

```html
<!DOCTYPE html>
<html lang="en">
<head>
<meta charset="utf-8">
<title>Marlowfen Pricing Counsel LLC</title>
<link rel="stylesheet" href="https://fonts.googleapis.com/css2?family=Poppins:wght@400;500;600;700;800&display=swap">
<style>
:root{
  --ink:#11122B;
  --brand:#4D6C8A;
  --navy:#2f4a6d;
  --navy-deep:#284262;
  --heading:#3b5679;
  --text:#3a3f4a;
  --white:#ffffff;
  --line:rgba(255,255,255,.75);
  --tile-label:#3e5c80;
}
*{box-sizing:border-box;margin:0;padding:0}
html,body{width:1200px;height:4380px;overflow:hidden}
body{font-family:"Poppins",sans-serif;color:var(--text);background:var(--white)}
section,header,footer{position:relative;width:1200px}
.band{background:linear-gradient(160deg,#2e4a6f 0%,#3f5e84 45%,#4D6C8A 100%)}

/* header */
.site-header{height:78px;background:var(--white)}
.brand{position:absolute;left:110px;top:12px;display:flex;align-items:center;gap:12px;color:var(--ink);font-weight:500}
.brand-mark{width:54px;height:54px;background:var(--ink)}
.brand-name{line-height:1}
.brand-name .big{display:block;font-size:34px;letter-spacing:.5px}
.brand-name .small{display:block;font-size:12px;letter-spacing:2px;margin-top:3px}
.menu-toggle{position:absolute;right:112px;top:30px;width:38px}
.menu-toggle span{display:block;height:3px;background:var(--ink);margin-bottom:6px;border-radius:2px}
.menu-toggle span:nth-child(2){width:30px;margin-left:8px}

/* hero */
.hero{height:638px;overflow:hidden}
.hero-photo{position:absolute;inset:0;background:linear-gradient(180deg,#9fb4c9 0%,#b99384 28%,#6e5c55 45%,#8a7a58 62%,#b0873f 78%,#6a5532 100%)}
.hero-copy{position:absolute;left:112px;top:298px;color:var(--white)}
.hero-copy h1{font-size:34px;font-weight:800;line-height:40px;text-transform:uppercase}
.hero-copy p{font-size:16px;margin-top:16px}
.btn-start{display:inline-block;margin-top:22px;background:var(--brand);color:var(--white);font-size:14px;font-weight:600;padding:14px 28px;border-radius:3px;letter-spacing:.5px}
.hero-arrow{position:absolute;top:376px}
.hero-arrow.prev{left:62px}.hero-arrow.next{right:62px}
.hero-dots{position:absolute;left:560px;top:674px;display:flex;gap:12px;top:674px}
.hero-dots{top:674px}
.hero-dots i{width:9px;height:9px;border-radius:50%;background:rgba(255,255,255,.5)}
.hero-dots i.on{background:var(--white)}

/* section titles */
.section-title{position:absolute;left:0;right:0;text-align:center;font-size:36px;font-weight:600;text-transform:uppercase}
.section-title::after{content:"";display:block;width:42px;height:3px;margin:12px auto 0;background:currentColor}
.band .section-title{color:var(--white)}
.light .section-title{color:var(--heading)}
.light .section-title::after{background:var(--heading)}

/* values */
.values{height:471px}
.values .section-title{top:92px}
.value-row{position:absolute;left:111px;top:182px;display:flex;gap:12px}
.value-box{width:187px;height:187px;border:1.5px solid var(--line);border-radius:3px;color:var(--white);text-align:center;padding-top:28px}
.value-box svg{width:86px;height:86px}
.value-box h3{font-size:17px;font-weight:600;margin-top:20px;text-transform:uppercase}

/* services */
.services{height:738px}
.services .section-title{top:74px}
.service-card{position:absolute;width:473px;height:225px;background:var(--white);box-shadow:0 2px 10px rgba(0,0,0,.12);padding:40px 24px 0 80px}
.service-card svg{position:absolute;left:12px;top:40px;width:60px;height:60px}
.service-card h3{font-size:18px;font-weight:600;color:var(--ink);text-transform:uppercase}
.service-card p{font-size:14px;line-height:24px;margin-top:4px;text-align:justify;color:#4a4f5a}
.c1{left:110px;top:166px}.c2{left:616px;top:166px}.c3{left:110px;top:428px}.c4{left:616px;top:428px}

/* clients */
.clients{height:515px}
.clients .section-title{top:88px}
.client-row{position:absolute;left:112px;top:188px;display:flex;gap:12px}
.client-box{width:235px;height:230px;border:1.5px solid var(--line);border-radius:3px;color:var(--white);text-align:center;padding-top:38px}
.client-box svg{width:84px;height:84px}
.client-box h3{font-size:16px;font-weight:600;line-height:26px;margin-top:20px;text-transform:uppercase}

/* industries */
.industries{height:936px}
.industries .section-title{top:72px;left:-20px}
.tile{position:absolute;width:312px;height:321px;overflow:hidden}
.tile .photo{height:265px}
.tile h3{height:56px;background:var(--tile-label);color:var(--white);font-size:19px;font-weight:600;text-transform:uppercase;display:flex;align-items:center;justify-content:center;text-align:center;line-height:21px}
.t1{left:110px;top:161px}.t2{left:444px;top:161px}.t3{left:778px;top:161px}
.t4{left:110px;top:506px}.t5{left:444px;top:506px}.t6{left:778px;top:506px}
.p-tech{background:linear-gradient(120deg,#1b2350,#2a4fb0 45%,#b0603a 75%,#1e2030)}
.p-manu{background:linear-gradient(180deg,#c9d2dc,#3a3f48 55%,#cfd6de)}
.p-whole{background:linear-gradient(160deg,#8a6a4e,#c79a72 50%,#a07a58)}
.p-biz{background:linear-gradient(160deg,#3a4658,#c9ccd1 55%,#e6e6e6)}
.p-retail{background:linear-gradient(160deg,#5a5048,#b9b3ad 50%,#3d3a38)}
.p-consumer{background:linear-gradient(160deg,#8c8f96,#b89880 55%,#6a6c74)}

/* contact */
.contact{height:575px}
.contact .section-title{top:80px}
.field{position:absolute;border:1.5px solid var(--line);color:var(--white);font-size:14px;padding:15px 12px}
.f1{left:206px;top:177px;width:386px;height:50px}
.f2{left:607px;top:177px;width:386px;height:50px}
.f3{left:206px;top:243px;width:386px;height:50px}
.f4{left:607px;top:243px;width:386px;height:50px}
.f5{left:206px;top:311px;width:788px;height:106px}
.captcha{position:absolute;left:420px;top:437px;width:207px;height:51px;background:#f7f7f7;border-radius:3px;display:flex;align-items:center;padding-left:10px;gap:8px;font-size:11px;color:#333}
.captcha i{width:18px;height:18px;border:2px solid #c1c1c1;background:var(--white);border-radius:2px}
.captcha b{position:absolute;right:12px;top:12px;width:24px;height:24px;border-radius:50%;background:#c9d3e0}
.btn-submit{position:absolute;left:638px;top:437px;width:144px;height:51px;background:var(--white);color:var(--navy);font-weight:600;font-size:15px;display:flex;align-items:center;justify-content:center;border-radius:3px}

/* footer */
.site-footer{height:429px;background:var(--navy-deep);color:var(--white)}
.foot-brand{position:absolute;left:110px;top:80px;display:flex;align-items:center;gap:8px;font-weight:500;color:var(--white)}
.foot-brand .mark{width:42px;height:42px;background:var(--white)}
.foot-brand .big{display:block;font-size:28px;line-height:28px}
.foot-brand .small{display:block;font-size:10px;letter-spacing:1.6px}
.follow{position:absolute;left:110px;top:152px;font-size:18px;font-weight:500}
.socials{position:absolute;left:110px;top:192px;display:flex;gap:10px}
.socials i{width:50px;height:50px;border-radius:50%;background:#4a6790}
.foot-col{position:absolute;top:70px}
.foot-col h4{font-size:18px;font-weight:500;text-transform:uppercase}
.foot-col h4::after{content:"";display:block;width:38px;height:2px;background:var(--white);margin-top:10px}
.quick{left:381px}
.quick ul{list-style:none;margin-top:8px}
.quick li{font-size:14px;line-height:33px}
.details{left:561px;width:300px}
.detail{display:flex;gap:14px;font-size:14px;line-height:23px;margin-top:18px;align-items:flex-start}
.detail .ico{flex:none;width:32px;height:32px;border-radius:50%;background:#4a6790;display:flex;align-items:center;justify-content:center}
.mapcol{left:879px}
.map{position:absolute;left:879px;top:117px;width:209px;height:211px;background:linear-gradient(135deg,#eef1f4,#dde3ea)}
.foot-rule{position:absolute;left:0;right:0;top:366px;height:1px;background:rgba(255,255,255,.15)}
.copyright{position:absolute;left:0;right:0;top:390px;text-align:center;font-size:13px}
</style>
</head>
<body>

<header class="site-header">
  <div class="brand">
    <span class="brand-mark"></span>
    <span class="brand-name"><span class="big">MARLOWFEN</span><span class="small">PRICING COUNSEL LLC</span></span>
  </div>
  <div class="menu-toggle"><span></span><span></span><span></span></div>
</header>

<section class="hero">
  <div class="hero-photo" role="img" aria-label="Mountain range at sunset above a road through golden grassland"></div>
  <div class="hero-copy">
    <h1>Building a Business<br>is a Journey</h1>
    <p>We have the valuation expertise to guide you.</p>
    <span class="btn-start">GET STARTED</span>
  </div>
  <svg class="hero-arrow prev" width="24" height="44" viewBox="0 0 24 44"><path d="M22 2 2 22l20 20" fill="none" stroke="#fff" stroke-width="2"/></svg>
  <svg class="hero-arrow next" width="24" height="44" viewBox="0 0 24 44"><path d="M2 2l20 20L2 42" fill="none" stroke="#fff" stroke-width="2"/></svg>
  <div class="hero-dots" style="top:596px"><i></i><i class="on"></i><i></i><i></i></div>
</section>

<section class="values band">
  <h2 class="section-title">Our Values</h2>
  <div class="value-row">
    <div class="value-box">
      <svg viewBox="0 0 80 80" fill="none" stroke="#fff" stroke-width="2.5"><circle cx="30" cy="30" r="10"/><circle cx="30" cy="30" r="18" stroke-dasharray="6 4"/><circle cx="55" cy="55" r="7"/><circle cx="55" cy="55" r="14" stroke-dasharray="5 4"/></svg>
      <h3>Integrity</h3>
    </div>
    <div class="value-box">
      <svg viewBox="0 0 80 80" fill="none" stroke="#fff" stroke-width="2.5"><circle cx="40" cy="40" r="34" stroke-dasharray="3 4"/><circle cx="28" cy="32" r="6"/><circle cx="40" cy="28" r="6"/><circle cx="52" cy="32" r="6"/><path d="M18 58c0-10 20-14 22-14s22 4 22 14"/><path d="M14 70h52"/></svg>
      <h3>Responsiveness</h3>
    </div>
    <div class="value-box">
      <svg viewBox="0 0 80 80" fill="none" stroke="#fff" stroke-width="2.5"><path d="M22 16h36l14 16-32 36L8 32z"/><path d="M8 32h64M30 16l-6 16 16 36 16-36-6-16"/></svg>
      <h3>Excellence</h3>
    </div>
    <div class="value-box">
      <svg viewBox="0 0 80 80" fill="none" stroke="#fff" stroke-width="2.5"><circle cx="40" cy="32" r="22" stroke-dasharray="6 4"/><circle cx="32" cy="28" r="5"/><circle cx="48" cy="28" r="5"/><path d="M10 60l14-10 16 10 16-10 14 10M24 50l-10 16M56 50l10 16"/></svg>
      <h3>Relationships</h3>
    </div>
    <div class="value-box">
      <svg viewBox="0 0 80 80" fill="none" stroke="#fff" stroke-width="2.5"><rect x="14" y="14" width="52" height="52" rx="4"/><path d="M14 30h16v20H14M66 30H50v20h16M30 14v16h20V14M30 66V50h20v16"/></svg>
      <h3>Community</h3>
    </div>
  </div>
</section>

<section class="services light">
  <h2 class="section-title">What We Do</h2>
  <div class="service-card c1">
    <svg viewBox="0 0 60 60" fill="none" stroke="#3b5679" stroke-width="2"><rect x="6" y="6" width="34" height="44" rx="2"/><path d="M12 22h22M12 30h22M12 38h14"/><circle cx="44" cy="44" r="10"/><path d="M39 44l4 4 6-8"/><text x="10" y="17" font-size="10" fill="#3b5679" stroke="none" font-family="Poppins,sans-serif">TAX</text></svg>
    <h3>Tax-Related Valuations</h3>
    <p style="text-align:left">Valuations for estate/gift tax, charitable contributions, equity-linked compensation, corporate restructuring and insolvency purposes.</p>
  </div>
  <div class="service-card c2">
    <svg viewBox="0 0 60 60" fill="none" stroke="#3b5679" stroke-width="2"><rect x="14" y="10" width="36" height="42" rx="2"/><circle cx="14" cy="18" r="9"/><path d="M14 9v9h9"/><path d="M20 44l8-10 6 6 10-12"/></svg>
    <h3>Financial Reporting</h3>
    <p>Our work includes purchase price allocations, fresh-start accounting, impairment analyses, equity-linked compensation, leases and financial instruments</p>
  </div>
  <div class="service-card c3">
    <svg viewBox="0 0 60 60" fill="none" stroke="#3b5679" stroke-width="2"><rect x="22" y="6" width="30" height="22" rx="2"/><path d="M28 13h18M28 20h12"/><circle cx="18" cy="26" r="6"/><path d="M6 48c0-8 6-12 12-12s12 4 12 12M36 40h18M8 54h46"/></svg>
    <h3>Financing &amp; Transaction Advisory</h3>
    <p>Financial assessments to evaluate debt structure &amp; capital adequacy. Valuation support for loan underwriting, capital raises, share redemptions, minority interest buyouts, buy-sell agreements as well as for mergers, acquisitions &amp; divestitures.</p>
  </div>
  <div class="service-card c4">
    <svg viewBox="0 0 60 60" fill="none" stroke="#3b5679" stroke-width="2"><circle cx="26" cy="20" r="9"/><circle cx="26" cy="20" r="3"/><circle cx="46" cy="12" r="5"/><circle cx="46" cy="30" r="5"/><path d="M6 44l12-4h14l8 4-10 6H12"/></svg>
    <h3>Business Planning &amp; Advisory</h3>
    <p>Outsourced financial planning &amp; analysis (FP&amp;A) services, including model development, strategy valuation and exit options analysis</p>
  </div>
</section>

<section class="clients band">
  <h2 class="section-title">Who Do We Serve</h2>
  <div class="client-row">
    <div class="client-box">
      <svg viewBox="0 0 80 80" fill="none" stroke="#fff" stroke-width="2.5"><circle cx="26" cy="18" r="10"/><circle cx="54" cy="18" r="10"/><path d="M8 60c0-14 8-22 18-22s18 8 18 22M36 60c0-14 8-22 18-22s18 8 18 22"/><circle cx="40" cy="48" r="6"/><path d="M30 76c0-8 4-12 10-12s10 4 10 12"/></svg>
      <h3>Family-Owned<br>Businesses</h3>
    </div>
    <div class="client-box">
      <svg viewBox="0 0 80 80" fill="none" stroke="#fff" stroke-width="3"><circle cx="40" cy="40" r="34"/><path d="M50 28c-2-4-6-6-10-6-6 0-10 3-10 8 0 11 20 7 20 18 0 5-4 8-10 8-4 0-8-2-10-6M40 16v48"/></svg>
      <h3>Private-Equity<br>Sponsored Companies</h3>
    </div>
    <div class="client-box">
      <svg viewBox="0 0 80 80" fill="none" stroke="#fff" stroke-width="2.5"><path d="M10 74h62M16 74V48h8v26M30 74V40h8v26M44 74V44h8v30M58 74V30h8v44"/><path d="M14 34l18-10 16 6 22-18"/><circle cx="14" cy="34" r="3"/><circle cx="32" cy="24" r="3"/><circle cx="48" cy="30" r="3"/><circle cx="70" cy="12" r="3"/></svg>
      <h3>Publicly Traded<br>Companies</h3>
    </div>
    <div class="client-box">
      <svg viewBox="0 0 80 80" fill="none" stroke="#fff" stroke-width="2.5"><path d="M36 6 8 22h56zM10 70h52M12 28v36M22 28v36M50 28v36M60 28v36"/><path d="M42 38c-2-3-10-3-10 2 0 6 10 4 10 10 0 5-8 5-10 2M37 34v22"/><rect x="56" y="52" width="18" height="6"/><rect x="56" y="60" width="18" height="6"/><rect x="56" y="68" width="18" height="6"/></svg>
      <h3>Lenders</h3>
    </div>
  </div>
</section>

<section class="industries light">
  <h2 class="section-title">Industries Served</h2>
  <div class="tile t1"><div class="photo p-tech" role="img" aria-label="Server room aisle lit in blue and orange"></div><h3>Technology</h3></div>
  <div class="tile t2"><div class="photo p-manu" role="img" aria-label="Automated machinery on a factory floor"></div><h3>Manufacturing</h3></div>
  <div class="tile t3"><div class="photo p-whole" role="img" aria-label="Warehouse stacked with cardboard boxes"></div><h3>Wholesale / Distribution</h3></div>
  <div class="tile t4"><div class="photo p-biz" role="img" aria-label="Business documents with charts on a desk"></div><h3>Business &amp; Professional<br>Services</h3></div>
  <div class="tile t5"><div class="photo p-retail" role="img" aria-label="Clothing shop counter with garments on racks"></div><h3>Retail</h3></div>
  <div class="tile t6"><div class="photo p-consumer" role="img" aria-label="Small business packing room with parcels"></div><h3>Consumer Products</h3></div>
</section>

<section class="contact band">
  <h2 class="section-title">Contact Us</h2>
  <div class="field f1">First Name</div>
  <div class="field f2">Last Name</div>
  <div class="field f3">Email</div>
  <div class="field f4">Phone</div>
  <div class="field f5">How Can We Help?</div>
  <div class="captcha"><i></i>I'm not a robot<b></b></div>
  <div class="btn-submit">SUBMIT</div>
</section>

<footer class="site-footer">
  <div class="foot-brand"><span class="mark"></span><span><span class="big">MARLOWFEN</span><span class="small">PRICING COUNSEL LLC</span></span></div>
  <div class="follow">FOLLOW US ON</div>
  <div class="socials" aria-label="Social media links"><i></i><i></i><i></i></div>

  <div class="foot-col quick">
    <h4>Quick Links</h4>
    <ul><li>Home</li><li>Our Values</li><li>What We Do</li><li>Who Do We Serve</li><li>Industries Served</li><li>Contact Us</li></ul>
  </div>

  <div class="foot-col details">
    <h4>Contact Details</h4>
    <div class="detail"><span class="ico"><svg width="14" height="18" viewBox="0 0 14 18"><path d="M7 0a7 7 0 0 0-7 7c0 5 7 11 7 11s7-6 7-11a7 7 0 0 0-7-7zm0 10a3 3 0 1 1 0-6 3 3 0 0 1 0 6z" fill="#fff"/></svg></span><span>1480 W Larkspur Ridge Ste 310,<br>Alderbrook, ID 83700</span></div>
    <div class="detail"><span class="ico"><svg width="16" height="16" viewBox="0 0 16 16"><path d="M3 1l3 3-2 2c1 2 3 4 6 6l2-2 3 3-2 2C7 15 1 9 1 3z" fill="#fff"/></svg></span><span style="line-height:32px">+1 208 555 0142</span></div>
    <div class="detail"><span class="ico"><svg width="16" height="12" viewBox="0 0 16 12"><rect width="16" height="12" rx="1" fill="#fff"/><path d="M1 1l7 6 7-6" fill="none" stroke="#4a6790" stroke-width="1.5"/></svg></span><span style="line-height:32px">hello@marlowfenpricing.com</span></div>
  </div>

  <div class="foot-col mapcol"><h4>Location Map</h4></div>
  <div class="map" role="img" aria-label="Street map showing the office location"></div>

  <div class="foot-rule"></div>
  <div class="copyright">© 2022marlowfenpricing. All Rights Reserved | Terms of Use | Privacy Policy</div>
</footer>

</body>
</html>
```